Birchwood Turf Care_2015 New Cards_V1

We need an enhanced business card from what we have today. We are a Landscaping company and we have an existing Logo and text info that we would like to include.
Text to include:
In business for over 20 years,Fully Insured, Weekly Lawn Maintenance, Spring & Fall Clean-up, Dale Whitford, 203-555-0147, www.birchwoodturfcarect.example, Visit our Website for additional Lawn Care Services or email directly at DALE@BIRCHWOODTURFCARE.EXAMPLE, We appreciate your business.
We want full color background and we will want to take this design and work with a printer that does high graphic silk screen cards. The colors we have thought about are Black, with our Green Logo, with Gold Text...we are open to different colors, we just want the card to wow!

Target Market(s)

Lawn Care Maintenance

Industry/Entity Type

Lawn Care

Contact Information for Business Card

Text to include:
In business for over 20 years, Fully Insured, Weekly Lawn Maintenance, Spring & Fall Clean-up, Dale Whitford, 203-555-0147, www.birchwoodturfcarect.example, Visit our Website for additional Lawn Care Services or email directly at DALE@BIRCHWOODTURFCARE.EXAMPLE, We appreciate your business.

Requirements
Must have
• Logo, text details about how to reach us, standard size business cards that go horizontal.
Nice to have
• background colors, background designs, raised embossed lettering, rounded corners(2 or 4),

```html
<!DOCTYPE html>
<html lang="en">
<head>
<meta charset="utf-8">
<title>Birchwood Turf Care – Business Card</title>
<link rel="stylesheet" href="https://fonts.googleapis.com/css2?family=Arimo:wght@400;700&display=swap">
<style>
  :root {
    --page-bg: #ece9e3;
    --card-white: #fbfbfa;
    --brand-green: #1f5a26;
    --brand-green-dark: #174a1d;
    --divider: #8aa88d;
    --grass-deep: #2f8f27;
    --grass-mid: #5cb232;
    --grass-light: #a9d63f;
    --text-on-grass: #ffffff;
    --card-shadow: rgba(40, 35, 25, 0.28);
  }
  * { box-sizing: border-box; margin: 0; padding: 0; }
  html, body {
    width: 1200px; height: 780px; overflow: hidden;
    background: var(--page-bg);
    font-family: "Arimo", Arial, sans-serif;
  }
  .sheet { position: relative; width: 1200px; height: 780px; }

  .card {
    position: absolute;
    width: 540px; height: 309px;
    border-radius: 20px;
    overflow: hidden;
    box-shadow: 0 10px 24px var(--card-shadow);
  }

  /* Front */
  .card-front { left: 40px; top: 170px; background: var(--card-white); }
  .front-brand {
    position: absolute; left: 34px; top: 0; width: 200px; height: 309px;
    display: flex; align-items: center; gap: 12px;
  }
  .brand-dot {
    flex: none; width: 20px; height: 20px; border-radius: 50%;
    background: var(--brand-green);
  }
  .brand-name {
    font-weight: 700; font-size: 26px; line-height: 1.15;
    color: var(--brand-green);
  }
  .front-divider {
    position: absolute; left: 252px; top: 62px; width: 1px; height: 185px;
    background: var(--divider);
  }
  .front-contact {
    position: absolute; left: 276px; top: 78px; right: 16px;
  }
  .contact-name {
    font-weight: 700; font-size: 25px; color: var(--brand-green);
    margin-bottom: 26px;
  }
  .contact-list { list-style: none; }
  .contact-item {
    display: flex; align-items: center; gap: 9px;
    font-size: 14.5px; color: var(--brand-green);
    margin-bottom: 9px; white-space: nowrap;
  }
  .contact-icon { flex: none; width: 16px; height: 16px; }

  /* Back */
  .card-back { left: 620px; top: 300px; }
  .grass-field {
    position: absolute; inset: 0;
    background:
      radial-gradient(ellipse at 78% 22%, var(--grass-light) 0%, rgba(169,214,63,0) 60%),
      linear-gradient(160deg, var(--grass-mid) 0%, var(--grass-deep) 100%);
  }
  .back-content {
    position: absolute; inset: 0;
    display: flex; flex-direction: column; align-items: center;
    padding-top: 58px; color: var(--text-on-grass);
  }
  .back-brand {
    display: flex; align-items: center; gap: 14px;
  }
  .back-brand .brand-dot { width: 26px; height: 26px; background: var(--text-on-grass); }
  .back-brand .brand-name { font-size: 40px; color: var(--text-on-grass); }
  .service-list {
    margin-top: 44px; width: 470px;
    font-size: 13.5px; line-height: 1.4;
    color: var(--text-on-grass);
  }
</style>
</head>
<body>
<main class="sheet">

  <section class="card card-front" aria-label="Business card front">
    <div class="front-brand">
      <span class="brand-dot"></span>
      <span class="brand-name">Birchwood Turf Care</span>
    </div>
    <div class="front-divider"></div>
    <div class="front-contact">
      <p class="contact-name">Dale Whitford</p>
      <ul class="contact-list">
        <li class="contact-item">
          <svg class="contact-icon" viewBox="0 0 16 16" aria-hidden="true">
            <rect width="16" height="16" rx="2" fill="#1f5a26"/>
            <path d="M5 3.5l2 2-1 1.2c.6 1.3 1.5 2.2 2.8 2.8L10 8.5l2 2-1.3 1.6C7.5 11.6 4.4 8.5 3.9 5.3z" fill="#fff"/>
          </svg>
          203-555-0147
        </li>
        <li class="contact-item">
          <svg class="contact-icon" viewBox="0 0 16 16" aria-hidden="true">
            <rect width="16" height="16" rx="2" fill="#1f5a26"/>
            <rect x="3" y="4.5" width="10" height="7" fill="none" stroke="#fff" stroke-width="1.2"/>
            <path d="M3 4.5l5 4 5-4" fill="none" stroke="#fff" stroke-width="1.2"/>
          </svg>
          dale@birchwoodturfcare.example
        </li>
        <li class="contact-item">
          <svg class="contact-icon" viewBox="0 0 16 16" aria-hidden="true">
            <rect width="16" height="16" rx="2" fill="#1f5a26"/>
            <circle cx="8" cy="8" r="5" fill="none" stroke="#fff" stroke-width="1.1"/>
            <ellipse cx="8" cy="8" rx="2.2" ry="5" fill="none" stroke="#fff" stroke-width="1"/>
            <path d="M3 8h10" stroke="#fff" stroke-width="1"/>
          </svg>
          www.birchwoodturfcarect.example
        </li>
      </ul>
    </div>
  </section>

  <section class="card card-back" aria-label="Business card back">
    <div class="grass-field" role="img" aria-label="Sunlit green lawn grass texture"></div>
    <div class="back-content">
      <div class="back-brand">
        <span class="brand-dot"></span>
        <span class="brand-name">Birchwood Turf Care</span>
      </div>
      <p class="service-list">
        Weekly Mowing | Spring &amp; Fall Clean-Ups | Mulching of Flower/Plant Beds<br>
        Edging | Hedge &amp; Shrub Trimming | Tree &amp; Shrub Plantings<br>
        Light Tree Trimming
      </p>
    </div>
  </section>

</main>
</body>
</html>
```